Flyer für KFZ-Gutachter
Zielgruppe
NFZ und KFZ Gutachten. Firma ist neu gegründet und Flyer wird benötigt um sich bei Werkstätten, Versicherungen und Privatkunden vorzustellen.
Aufgabenstellung
Es soll elegant, klassisch sein und angelehnt sein an meine Website https://www.holvarentis.de/ Handynummer 0157 - 62830417 bitte einpflegen. Außerdem sollten die Logos des Bundesverbandes und der Zertifizierung mit im Flyer eingebunden werden. Diese lade ich hoch. Auch das korrekte Logo lade ich hoch.

```html
<!DOCTYPE html>
<html lang="de">
<head>
<meta charset="utf-8">
<title>Holvarentis – Flyer</title>
<link href="https://fonts.googleapis.com/css2?family=Noto+Serif:wght@300;400;600&display=swap" rel="stylesheet">
<style>
  :root{
    --page:#f2f2f1;
    --band-light:#e6e6e6;
    --ink:#1d1d1d;
    --white:#ffffff;
    --card:#f7f7f7;
    --photo-top:#727a76;
    --photo-bottom:#5f6663;
    --shirt:#8eaed6;
    --muted:#5a5a5a;
    --badge-a:#2f7dbf;
    --badge-b:#8aa2c7;
  }
  *{margin:0;padding:0;box-sizing:border-box}
  html,body{width:1080px;height:1200px;overflow:hidden;background:var(--page)}
  body{font-family:"Noto Serif",Georgia,serif;color:var(--ink)}
  .flyer{position:absolute;left:140px;top:33px;width:800px;height:1133px;background:var(--band-light);overflow:hidden}
  .flyer-photo{position:absolute;left:0;top:0;width:800px;height:800px;
    background:radial-gradient(ellipse 45% 55% at 48% 78%, var(--shirt) 0%, rgba(142,174,214,.55) 55%, transparent 80%),
               linear-gradient(180deg,var(--photo-top),var(--photo-bottom));
    clip-path:polygon(0 164px,800px 104px,800px 691px,0 776px)}
  .flyer-footer{position:absolute;left:0;top:922px;width:800px;height:211px;background:var(--ink)}
  .brand-box{position:absolute;left:274px;top:0;width:258px;height:218px;background:var(--ink);
    display:flex;flex-direction:column;align-items:center;justify-content:center;gap:14px}
  .brand-mark{width:26px;height:26px;border:2px solid var(--white)}
  .brand-name{color:var(--white);font-size:26px;font-weight:600;letter-spacing:3px;white-space:nowrap}
  .headline{position:absolute;left:0;width:800px;top:470px;text-align:center;color:var(--white);
    font-size:43px;font-weight:400;text-shadow:0 2px 6px rgba(0,0,0,.35);white-space:nowrap}
  .headline-rule{position:absolute;left:442px;top:540px;width:196px;height:1px;background:rgba(255,255,255,.7)}
  .subline{position:absolute;right:163px;top:560px;text-align:right;color:#eef0f2;font-size:20px;font-weight:300;line-height:1.2}
  .service{position:absolute;background:var(--card);text-align:center;padding:0 14px;box-shadow:0 1px 4px rgba(0,0,0,.08)}
  .service svg{display:block;margin:0 auto}
  .service-title{font-size:15px;font-weight:600;margin-top:16px;white-space:nowrap}
  .service-rule{width:78px;height:1px;background:var(--ink);margin:18px auto 16px}
  .service-text{font-size:10.5px;line-height:1.25;color:var(--muted);text-align:left}
  .service--accident{left:102px;top:653px;width:182px;height:289px;padding-top:44px}
  .service--value{left:308px;top:635px;width:185px;height:325px;padding-top:62px}
  .service--damage{left:521px;top:653px;width:182px;height:289px;padding-top:44px}
  .phone{position:absolute;left:58px;top:984px;width:278px;height:50px;background:var(--white);
    display:flex;align-items:center;gap:14px;padding-left:18px;font-size:25px;line-height:1;white-space:nowrap;overflow:hidden}
  .phone svg{flex:none}
  .address{position:absolute;left:58px;top:1050px;color:var(--white);font-size:20px;font-weight:300;white-space:nowrap}
  .web{position:absolute;left:58px;top:1086px;color:#d9d9d9;font-size:11px;letter-spacing:7px;white-space:nowrap}
  .badges{position:absolute;left:472px;top:1002px;width:328px;height:73px;background:var(--white);
    display:flex;align-items:center;padding-left:36px;gap:22px}
  .badge-round{flex:none;width:46px;height:46px;border-radius:50%;background:var(--badge-a);border:3px solid #d7c35a}
  .badge-oval{flex:none;width:68px;height:46px;border-radius:50%;background:#fff;border:3px solid var(--badge-b)}
  .expert{display:flex;gap:8px;align-items:flex-start}
  .flag{flex:none;width:3px;height:46px;background:linear-gradient(180deg,#111 0 33%,#d6232a 33% 66%,#f5c400 66%)}
  .expert-name{font-size:12px;line-height:1.2;white-space:nowrap}
  .expert-note{font-size:5.5px;line-height:1.25;color:var(--muted);width:84px}
</style>
</head>
<body>
<main class="flyer">
  <div class="flyer-photo" role="img" aria-label="Foto: zwei Sachverständige in hellblauen Hemden vor grauem Hintergrund"></div>
  <div class="flyer-footer"></div>

  <header class="brand-box">
    <span class="brand-mark"></span>
    <span class="brand-name">HOLVARENTIS</span>
  </header>

  <h1 class="headline">Ihr Experte für Gutachten</h1>
  <div class="headline-rule"></div>
  <p class="subline">Präzise Bewertungen<br>für Ihre Bedürfnisse</p>

  <section class="service service--accident">
    <svg width="44" height="38" viewBox="0 0 44 38"><path d="M4 30V20l4-8h14l4 8v10z" fill="#1d1d1d"/><circle cx="10" cy="31" r="4" fill="#1d1d1d"/><circle cx="22" cy="31" r="4" fill="#1d1d1d"/><path d="M28 24l6-2 2-6 3 6 5 1-4 4" fill="none" stroke="#1d1d1d" stroke-width="2"/></svg>
    <h2 class="service-title">Unfallgutachten</h2>
    <div class="service-rule"></div>
    <p class="service-text">Wir erstellen detaillierte Unfall­gutachten, die Ihnen bei der Schadensregulierung helfen und für Versicherungen präzise nachvollziehbar sind.</p>
  </section>

  <section class="service service--value">
    <svg width="40" height="32" viewBox="0 0 40 32"><path d="M4 26V16l5-11h22l5 11v10z" fill="#1d1d1d"/><rect x="11" y="8" width="18" height="7" fill="#fff"/><circle cx="10" cy="20" r="2.5" fill="#fff"/><circle cx="30" cy="20" r="2.5" fill="#fff"/><rect x="5" y="26" width="6" height="5" fill="#1d1d1d"/><rect x="29" y="26" width="6" height="5" fill="#1d1d1d"/></svg>
    <h2 class="service-title">Wertgutachten</h2>
    <div class="service-rule"></div>
    <p class="service-text">Erhalten Sie fundierte Wertgut­achten, die Ihnen bei Kaufent­scheidungen oder bei der Schadenregulierung nützlich sein können.</p>
  </section>

  <section class="service service--damage">
    <svg width="44" height="38" viewBox="0 0 44 38"><path d="M4 6l8 8M9 3l7 8M14 2l5 7" stroke="#1d1d1d" stroke-width="2"/><path d="M16 32V22l4-8h14l4 8v10z" fill="#1d1d1d"/><circle cx="22" cy="33" r="4" fill="#1d1d1d"/></svg>
    <h2 class="service-title">Schadensgutachten</h2>
    <div class="service-rule"></div>
    <p class="service-text">Präzise Schadensgutachten, die alle relevanten Informationen enthalten und die rechtlichen Anforderungen erfüllen.</p>
  </section>

  <div class="phone">
    <svg width="22" height="22" viewBox="0 0 24 24"><path d="M6.6 10.8a15 15 0 0 0 6.6 6.6l2.2-2.2c.3-.3.7-.4 1-.2 1.1.4 2.3.6 3.6.6.6 0 1 .4 1 1V20c0 .6-.4 1-1 1C10.6 21 3 13.4 3 4c0-.6.4-1 1-1h3.5c.6 0 1 .4 1 1 0 1.3.2 2.5.6 3.6.1.3 0 .7-.2 1z" fill="#1d1d1d"/></svg>
    <span>0157 628 304 17</span>
  </div>
  <p class="address">Birkenallee 18 — 71034 Feldhausen</p>
  <p class="web">WWW.HOLVARENTIS.DE</p>

  <aside class="badges">
    <span class="badge-round"></span>
    <span class="badge-oval"></span>
    <div class="expert">
      <span class="flag"></span>
      <div>
        <p class="expert-name">Dorian Mekaj</p>
        <p class="expert-note">Geprüfter Sachverständiger für Nutzfahrzeuge, Kfz-Schäden und Bewertung</p>
      </div>
    </div>
  </aside>
</main>
</body>
</html>
```